VEXO Transaction Systems Corprate Web Site

Develop new corporate website and copywriting of web site. VEXO provides MPOS for banks and payment processors. Have included corporate background as well as marketing material from a bank payment processor that uses our products and services.

VEXO Transaction Systems Web design.... We are looking for a solid design to be followed by a complete proposal to complete entire site. The budget proposed is for design only to be followed by a complete budget.

tom questions Tom.Garrity@vexotsys.example

This is not really up to date as its our corporate website.... www.vexotransactionsystems.example

This is a customer that uses software that VEXO developed and that we have white labeled.
http://support.fenwara.example/en/fenwara-handheld/fenwara-handheld-max

We are open to new logo design (the current logo has many good design elements with the "Locked Tile"). We have provided what we use now in logo.zip. We use as example "Integrated Payment Solutions" as a tag line. We would also use Mobile as well as Transportation Solutions.
Updates

VEXO Transaction Systems Web design.... We are looking for a solid design to be followed by a complete proposal to complete entire site. The budget proposed is for design only to be followed by a complete budget.tom questions Tom.Garrity@vexotsys.example Added Sunday, September 13, 2015

Target Market(s)

Banks, payment processors and enterprise customers...

Coding

Coded - Design and coding required

Number of Pages Required

5+ page

Requirements
Must have
• VEXO Transaction Systems Web design.... We are looking for a solid design to be followed by a complete proposal to complete entire site. The budget proposed is for design only to be followed by a complete budget.
• tom questions Tom.Garrity@vexotsys.example
Nice to have

```html
<!DOCTYPE html>
<html lang="en">
<head>
<meta charset="utf-8">
<title>VEXO Transaction Systems – Integrated Payment Solutions</title>
<link href="https://fonts.googleapis.com/css2?family=Raleway:wght@400;500;600;700&family=Open+Sans:wght@400;600&display=swap" rel="stylesheet">
<style>
:root{
  --orange:#f47c20;
  --orange-dark:#d9661a;
  --ink:#2d2d2d;
  --muted:#8a8a8a;
  --dark:#2a2420;
  --line:#e3e3e3;
  --footer:#ebebeb;
  --white:#ffffff;
}
*{box-sizing:border-box;margin:0;padding:0}
html,body{width:1200px;height:3472px;overflow:hidden}
body{font-family:"Open Sans",Arial,sans-serif;color:var(--ink);background:var(--white);position:relative}
h1,h2,h3,h4,.nav,.btn{font-family:"Raleway",Arial,sans-serif}
.abs{position:absolute}
.btn{display:inline-block;background:var(--orange);color:var(--white);font-size:13px;font-weight:700;letter-spacing:1px;padding:14px 30px;text-transform:uppercase}

/* header */
.site-header{top:0;left:0;width:1200px;height:90px;background:var(--white);display:flex;align-items:center;justify-content:space-between;padding:0 100px;box-shadow:0 2px 6px rgba(0,0,0,.08);z-index:2}
.brand{display:flex;align-items:center;gap:10px;font-family:"Raleway",sans-serif;font-weight:700;font-size:30px;color:var(--ink)}
.brand-dot{width:34px;height:34px;border-radius:50%;background:var(--orange)}
.nav{display:flex;align-items:center;gap:40px;font-size:12px;font-weight:600;letter-spacing:1px;color:var(--ink)}
.nav .btn{padding:10px 28px;font-size:12px}

/* hero */
.hero{top:90px;left:0;width:1200px;height:510px;background:linear-gradient(100deg,#3a332e 0%,#4c4540 45%,#6c635b 70%,#3b3430 100%)}
.hero-device{top:130px;left:760px;width:250px;height:440px;background:linear-gradient(160deg,#8a8078,#c9bfb4 55%,#6d645d);border-radius:30px;opacity:.85}
.hero-copy{top:270px;left:100px;width:520px;color:var(--white)}
.hero-copy h1{font-size:48px;font-weight:500;line-height:1}
.hero-copy h1 b{font-weight:700}
.hero-copy h1 span{font-size:32px}
.hero-copy p{font-size:13px;line-height:1.5;margin:16px 0 24px;opacity:.85}
.hero-platforms{top:410px;left:100px;color:var(--white)}
.hero-platforms h2{font-size:40px;font-weight:400}
.platform-tags{display:flex;gap:26px;margin-top:30px}
.platform-tags div{display:flex;align-items:center;gap:8px;font-family:"Raleway",sans-serif;font-weight:600;font-size:16px}
.platform-tags i{width:30px;height:30px;border-radius:50%;background:var(--white);opacity:.9}

/* white paper intro */
.intro{top:650px;left:0;width:1200px;height:220px}
.intro-mark{top:20px;left:220px;width:170px;height:170px;border-radius:50%;background:var(--dark);display:flex;align-items:center;justify-content:center;font-family:"Raleway",sans-serif;font-weight:700;font-size:40px;color:var(--white)}
.intro-copy{top:40px;left:400px;width:620px}
.intro-copy h2{font-size:24px;font-weight:600;line-height:1.35;color:#444}
.intro-copy p{font-size:12px;line-height:1.6;color:var(--muted);margin-top:12px}

/* white papers */
.papers{top:870px;left:0;width:1200px;text-align:center}
.section-title{font-size:24px;font-weight:600;letter-spacing:1px;color:#333;text-transform:uppercase}
.section-sub{width:760px;margin:14px auto 0;font-size:12px;line-height:1.6;color:var(--muted)}
.paper-grid{top:1020px;left:100px;width:1000px;display:grid;grid-template-columns:repeat(4,1fr);row-gap:60px;column-gap:20px}
.paper{display:grid;grid-template-columns:36px 1fr;column-gap:10px}
.paper svg{width:28px;height:28px}
.paper h3{font-size:16px;font-weight:600;color:#333;align-self:center}
.paper p{grid-column:2;font-size:11px;line-height:1.6;color:var(--muted);margin-top:8px}

/* platforms */
.platforms{top:1400px;left:0;width:1200px;height:620px;background:linear-gradient(180deg,#2c2622,#3a322c 50%,#2a2420)}
.platforms .section-title{color:var(--white);text-align:center;margin-top:60px}
.platforms .rule{width:1000px;height:1px;background:rgba(255,255,255,.2);margin:24px auto 0}
.platform{position:absolute;top:210px;width:340px;text-align:center;color:var(--white)}
.platform-icon{width:160px;height:160px;border-radius:50%;border:4px solid var(--orange);margin:0 auto;display:flex;align-items:center;justify-content:center}
.platform-icon span{width:130px;height:130px;border-radius:50%;background:var(--orange);display:flex;align-items:center;justify-content:center;font-family:"Raleway",sans-serif;font-weight:600;font-size:22px}
.platform h3{font-size:22px;font-weight:500;margin-top:30px}
.platform p{font-size:12px;line-height:1.6;opacity:.8;margin-top:12px}

/* portals */
.portals{top:2160px;left:100px;width:460px}
.portals h4{font-size:20px;font-weight:600;color:#333}
.portals h2{font-size:34px;font-weight:700;color:#222;letter-spacing:1px}
.portals .lead{font-size:12px;line-height:1.6;color:#555;margin-top:18px}
.portals ul{list-style:none;margin:16px 0 30px}
.portals li{font-size:12px;line-height:1.6;color:var(--muted);padding-left:20px;position:relative;margin-bottom:6px}
.portals li:before{content:"";position:absolute;left:0;top:6px;width:8px;height:8px;border-radius:50%;background:var(--orange)}
.portal-screens{top:2110px;left:600px;width:520px;height:460px;background:linear-gradient(160deg,#f1f1f1,#d8d8d8);border-radius:6px}

/* testimonials */
.clients{top:2668px;left:0;width:1200px;text-align:center}
.client-row{top:2760px;left:100px;width:1000px;display:grid;grid-template-columns:repeat(3,1fr);gap:40px}
.client{display:grid;grid-template-columns:70px 1fr;column-gap:16px}
.avatar{width:70px;height:70px;border-radius:50%;background:linear-gradient(160deg,#c9a68a,#6e5444)}
.client h4{font-size:14px;font-weight:600;color:var(--orange)}
.client small{display:block;font-size:11px;color:var(--muted);margin:2px 0 8px}
.client p{font-size:11px;line-height:1.6;color:var(--muted)}

/* partners */
.partners{top:2955px;left:0;width:1200px;text-align:center}
.partners h2{font-size:18px;font-weight:600;color:#444;text-transform:uppercase;letter-spacing:1px}
.partner-row{top:3020px;left:0;width:1200px;display:flex;justify-content:center;gap:110px;align-items:center}
.partner{font-family:"Raleway",sans-serif;font-weight:700;font-size:34px;color:#333;display:flex;align-items:center;gap:10px}
.partner i{width:22px;height:22px;border-radius:50%;background:var(--orange)}

/* footer */
.site-footer{top:3140px;left:0;width:1200px;height:300px;background:var(--footer);padding:60px 100px 0;display:grid;grid-template-columns:420px 170px 170px 1fr;column-gap:30px}
.site-footer h5{font-family:"Raleway",sans-serif;font-size:14px;font-weight:700;color:var(--orange);margin-bottom:14px}
.site-footer p,.site-footer li{font-size:12px;line-height:1.8;color:#666;list-style:none}
.social{display:flex;gap:8px;margin-bottom:20px}
.social i{width:22px;height:22px;border-radius:50%;background:var(--orange)}
.footer-brand{display:flex;align-items:center;gap:8px;font-family:"Raleway",sans-serif;font-weight:700;font-size:30px;color:var(--ink)}
.footer-brand i{width:30px;height:30px;border-radius:50%;background:var(--dark)}
.copyright{top:3440px;left:0;width:1200px;height:32px;background:#dedede;font-size:11px;color:#777;text-align:center;line-height:32px}
</style>
</head>
<body>

<header class="site-header abs">
  <div class="brand"><span class="brand-dot"></span>VEXO</div>
  <nav class="nav">
    <span>HOME</span><span>SERVICES</span><span>WHITE PAPERS</span><span>ABOUT US</span><span>CONTACT US</span>
    <span class="btn">Login</span>
  </nav>
</header>

<section class="hero abs" role="img" aria-label="Hand holding a smartphone showing the payment app in a softly lit shop interior"></section>
<div class="hero-device abs" role="img" aria-label="Smartphone with payment application screen"></div>
<div class="hero-copy abs">
  <h1><b>VEXO</b><span>Integrated Payment Solutions</span></h1>
  <p>We provide mobility and MOBILE services, e-ticketing, expense management and payment systems that help banks and processors grow their reach.</p>
  <span class="btn">View more info</span>
</div>
<div class="hero-platforms abs" style="top:500px">
  <h2>Supported Mobile Platforms</h2>
  <div class="platform-tags"><div><i></i>Andros</div><div><i></i>Ionix</div></div>
</div>

<section class="intro abs">
  <div class="intro-mark abs">VEXO</div>
  <div class="intro-copy abs">
    <h2>MOBILE AND PORTAL BUSINESS APPLICATION'S<br>PRODUCT WHITE PAPER</h2>
    <p>VEXO provides mobility and MPOS services, e-ticketing, expense management and payment systems (Mobile POS and Closed Loop NFC Payments) with a focus on partnering with banks to automate business and deepen customer relationships. Our team is the fast and easy way to deliver complete payment solutions.</p>
  </div>
</section>

<section class="papers abs">
  <h2 class="section-title">White Papers</h2>
  <p class="section-sub">VEXO provides mobility and MPOS services, e-ticketing, expense management and payment systems (Mobile POS and Closed Loop NFC Payments) with a focus on our partners to automate business and deepen customer relationships for banks.</p>
</section>

<div class="paper-grid abs">
  <div class="paper">
    <svg viewBox="0 0 28 28"><circle cx="14" cy="14" r="11" fill="none" stroke="var(--orange)" stroke-width="2"/><path d="M14 8v6l4 3" stroke="var(--orange)" stroke-width="2" fill="none"/></svg>
    <h3>News Emerging</h3><p>Short notes on the latest trends in mobile payment and card acceptance markets.</p>
  </div>
  <div class="paper">
    <svg viewBox="0 0 28 28"><rect x="3" y="5" width="22" height="16" rx="2" fill="none" stroke="var(--orange)" stroke-width="2"/><path d="M9 25h10" stroke="var(--orange)" stroke-width="2"/></svg>
    <h3>Web portal</h3><p>One secure portal to manage merchants, devices and reports across every branch.</p>
  </div>
  <div class="paper">
    <svg viewBox="0 0 28 28"><circle cx="9" cy="10" r="4" fill="none" stroke="var(--orange)" stroke-width="2"/><circle cx="19" cy="10" r="4" fill="none" stroke="var(--orange)" stroke-width="2"/><path d="M3 23c1-5 11-5 12 0M13 23c1-5 11-5 12 0" fill="none" stroke="var(--orange)" stroke-width="2"/></svg>
    <h3>Partnering</h3><p>We work with banks and processors to launch white labeled solutions quickly.</p>
  </div>
  <div class="paper">
    <svg viewBox="0 0 28 28"><path d="M4 22l7-7 5 4 8-10" fill="none" stroke="var(--orange)" stroke-width="2"/></svg>
    <h3>Capture and manage liquidity</h3><p>Real time views of funds, settlements and daily cash flow for businesses.</p>
  </div>
  <div class="paper">
    <svg viewBox="0 0 28 28"><circle cx="14" cy="14" r="11" fill="none" stroke="var(--orange)" stroke-width="2"/><circle cx="14" cy="14" r="4" fill="var(--orange)"/></svg>
    <h3>VEXO ecosystem</h3><p>Apps, devices and portals that connect into one complete payment platform.</p>
  </div>
  <div class="paper">
    <svg viewBox="0 0 28 28"><rect x="4" y="4" width="8" height="8" fill="none" stroke="var(--orange)" stroke-width="2"/><rect x="16" y="4" width="8" height="8" fill="none" stroke="var(--orange)" stroke-width="2"/><rect x="4" y="16" width="8" height="8" fill="none" stroke="var(--orange)" stroke-width="2"/><rect x="16" y="16" width="8" height="8" fill="none" stroke="var(--orange)" stroke-width="2"/></svg>
    <h3>Modular services</h3><p>Choose only the modules you need and add more as your program grows.</p>
  </div>
  <div class="paper">
    <svg viewBox="0 0 28 28"><rect x="4" y="4" width="20" height="20" rx="2" fill="none" stroke="var(--orange)" stroke-width="2"/><path d="M8 14l4 4 8-8" fill="none" stroke="var(--orange)" stroke-width="2"/></svg>
    <h3>VEXO Customised</h3><p>Branding, workflows and features tailored to each partner and region.</p>
  </div>
  <div class="paper">
    <svg viewBox="0 0 28 28"><path d="M4 14h18M16 8l6 6-6 6" fill="none" stroke="var(--orange)" stroke-width="2"/></svg>
    <h3>Quick to market</h3><p>Proven software lets partners launch new payment services within weeks.</p>
  </div>
</div>

<section class="platforms abs" role="img" aria-label="Dark background of a keyboard and mouse on a desk">
  <h2 class="section-title">Supported Mobile Platforms</h2>
  <div class="rule"></div>
  <div class="platform" style="left:200px">
    <div class="platform-icon"><span>Andros</span></div>
    <h3>Andros Mobile Platforms</h3>
    <p>VEXO provides mobility and MPOS services, e-ticketing, expense management and payment systems (Mobile POS and Closed Loop NFC Payments) with a focus on our partners to automate business and deepen customer relationships for banks.</p>
  </div>
  <div class="platform" style="left:660px">
    <div class="platform-icon"><span>Ionix</span></div>
    <h3>Ionix Mobile Platforms</h3>
    <p>VEXO provides mobility and MPOS services, e-ticketing, expense management and payment systems (Mobile POS and Closed Loop NFC Payments) with a focus on our partners to automate business and deepen customer relationships for banks.</p>
  </div>
</section>

<section class="portals abs">
  <h4>VEXO MANAGEMENT PORTALS</h4>
  <h2>FEATURES</h2>
  <p class="lead">Web are where Portal (PM) and Web License Operations<br>Management of Portal Admin users with profiles, provides limits on access</p>
  <ul>
    <li>Create and Manage Merchant Profiles and Receipt parameters for merchants' users</li>
    <li>Daily Import Merchant Profiles</li>
    <li>Manage merchant transaction reports for Debit and Credit with filters by Merchant, Date, Terminal ID and Transaction Types such as Cash, EBT/Credit and Cheque</li>
  </ul>
  <span class="btn">View more info</span>
</section>
<div class="portal-screens abs" role="img" aria-label="Desktop monitor, tablet and phone showing the management portal dashboard"></div>

<section class="clients abs">
  <h2 class="section-title">What Our Client's Say</h2>
</section>
<div class="client-row abs">
  <div class="client"><div class="avatar" role="img" aria-label="Client portrait"></div><div><h4>Darren Marsh</h4><small>Operations Lead</small><p>VEXO helped us launch mobile payments for our merchants quickly and the support team was always available.</p></div></div>
  <div class="client"><div class="avatar" role="img" aria-label="Client portrait"></div><div><h4>Karen Rolfe</h4><small>Product Manager</small><p>The portal gives our staff a clear view of every terminal and transaction, saving hours each week.</p></div></div>
  <div class="client"><div class="avatar" role="img" aria-label="Client portrait"></div><div><h4>Simon Hale</h4><small>Payments Director</small><p>A reliable partner with proven software that our bank could brand and bring to market fast.</p></div></div>
</div>

<section class="partners abs">
  <h2>Your partner supporting business and enterprise</h2>
</section>
<div class="partner-row abs">
  <div class="partner"><i></i>VEXO</div>
  <div class="partner"><i></i>Transity</div>
  <div class="partner"><i></i>Fenwara</div>
</div>

<footer class="site-footer abs">
  <div>
    <h5>About VEXO Transaction Systems</h5>
    <p>VEXO provides mobility and MPOS services, e-ticketing, expense management and payment systems (Mobile POS and Closed Loop NFC Payments) with a focus on our partners to automate business and deepen customer relationships. Our team is the fast and easy way to deliver a competitive business solution.</p>
  </div>
  <div>
    <h5>Website</h5>
    <ul><li>Home</li><li>Services</li><li>White Papers</li><li>About Us</li><li>Contact Us</li></ul>
  </div>
  <div>
    <h5>Information</h5>
    <ul><li>Terms &amp; Conditions</li><li>Privacy Policy</li><li>Solutions</li><li>Sitemap</li></ul>
  </div>
  <div>
    <h5>Follow Us</h5>
    <div class="social"><i></i><i></i><i></i><i></i><i></i></div>
    <div class="footer-brand"><i></i>VEXO</div>
  </div>
</footer>
<div class="copyright abs">© 2015 VEXO Transaction Systems. All rights reserved.</div>

</body>
</html>
```